Auto Insurance Flyer

Target Market(s)

english/spanish

Industry/Entity Type

Insurance Broker

Font styles to use
Serif

Colors

Designer to choose colors to be used in the design.

Requirements
Must have
• blend with my logo colors
Nice to have
• Eye catching call to action. Attention grabbers

```html
<!DOCTYPE html>
<html lang="en">
<head>
<meta charset="utf-8">
<title>Auto Insurance Flyer</title>
<link href="https://fonts.googleapis.com/css2?family=Crimson+Pro:wght@400;600;700&display=swap" rel="stylesheet">
<style>
  :root{
    --navy:#08111f;
    --navy-2:#0d2138;
    --ring-navy:#123556;
    --tan:#c49a6c;
    --pill:#1b5478;
    --ink:#141c2a;
    --white:#ffffff;
    --stage:#e6e6e6;
    --car-light:#f5f5f3;
    --car-mid:#dcdfe2;
    --car-shade:#b9bec4;
  }
  *{margin:0;padding:0;box-sizing:border-box}
  html,body{width:1200px;height:1200px;overflow:hidden;background:var(--stage)}
  body{font-family:"Crimson Pro",Georgia,serif;position:relative}
  .flyer{position:absolute;left:17px;top:222px;width:1166px;height:756px;overflow:hidden;
    background:radial-gradient(ellipse at 70% 40%,var(--navy-2) 0%,var(--navy) 70%)}
  .shapes{position:absolute;inset:0}
  .abs{position:absolute}

  .headline{left:118px;top:22px;display:flex;align-items:flex-start;gap:22px;color:var(--tan)}
  .headline-dui{font-size:104px;font-weight:700;line-height:1;letter-spacing:1px}
  .headline-sub{color:var(--white);font-weight:700;font-size:41px;line-height:.98;padding-top:26px;letter-spacing:.5px}

  .perks{left:118px;top:164px;color:var(--white);font-size:18px;line-height:32px;list-style:none}
  .perks li{display:inline-block;margin-right:22px}
  .perks li::before,.services li::before{content:"";display:inline-block;width:8px;height:8px;border-radius:50%;
    background:var(--tan);margin-right:12px;vertical-align:middle;position:relative;top:-2px}

  .car-shadow{left:70px;top:560px;width:520px;height:70px;border-radius:50%;
    background:radial-gradient(ellipse closest-side,rgba(0,0,0,.55),rgba(0,0,0,0));}
  .car-photo{left:44px;top:282px;width:560px;height:320px;border-radius:38% 34% 14% 18% / 42% 40% 20% 22%;
    background:linear-gradient(170deg,var(--car-light) 0%,var(--car-mid) 55%,var(--car-shade) 100%)}

  .brand{left:732px;top:48px;width:392px;text-align:center;color:var(--tan)}
  .brand-mark{width:62px;height:62px;border-radius:50%;background:var(--tan);margin:0 auto 14px}
  .brand-name{font-size:22px;font-weight:600;letter-spacing:1.5px;line-height:1.15;text-transform:uppercase}

  .intro{left:732px;top:206px;width:392px;color:var(--white);font-size:17.5px;line-height:23px;text-align:justify}

  .services-title{left:727px;top:356px;color:var(--tan);font-size:18.5px;font-weight:400;text-transform:uppercase}
  .services{left:730px;top:386px;color:var(--white);font-size:17.5px;line-height:32px;list-style:none}
  .services .more{padding-left:20px;line-height:20px}
  .services .more::before{display:none}

  .card-photo{left:963px;width:154px;border-radius:5px}
  .card-benefits{top:344px;height:96px;background:linear-gradient(160deg,#b06a3a 0%,#6d4c3b 50%,#8aa7bf 100%)}
  .card-id{top:447px;height:96px;background:linear-gradient(180deg,#ffffff 0%,#e9eef5 100%)}

  .offices{right:44px;top:574px;text-align:right;font-weight:700;letter-spacing:1px}
  .offices-title{color:var(--white);font-size:16px;text-transform:uppercase}
  .offices-list{color:var(--ink);font-size:16px;margin-top:4px}

  .call{right:42px;top:644px;text-align:right}
  .call-title{color:var(--tan);font-size:23px;font-weight:700;text-transform:uppercase}
  .call-phones{color:var(--white);font-size:20px;font-weight:700;letter-spacing:1px;margin-top:2px}

  .quote{left:44px;top:674px;display:flex;align-items:center;gap:12px}
  .quote-label{color:var(--ink);font-size:20px;font-weight:700;text-transform:uppercase}
  .quote-url{background:var(--pill);color:var(--white);font-size:17px;font-weight:700;letter-spacing:.5px;
    padding:4px 16px;border-radius:18px}
</style>
</head>
<body>
<main class="flyer">
  <svg class="shapes" width="1166" height="756" viewBox="0 0 1166 756" aria-hidden="true">
    <circle cx="346" cy="126" r="346" fill="none" stroke="var(--tan)" stroke-width="20"/>
    <circle cx="346" cy="126" r="318" fill="none" stroke="var(--ring-navy)" stroke-width="6"/>
    <path d="M0,386 Q320,350 540,500 Q710,620 776,756 L0,756 Z" fill="var(--tan)"/>
    <polygon points="661,571 1166,571 1166,631 721,631" fill="var(--tan)"/>
  </svg>

  <div class="abs headline">
    <span class="headline-dui">DUI</span>
    <span class="headline-sub">NO<br>PROBLEM</span>
  </div>

  <ul class="abs perks">
    <li>Foreign License-No problem</li><li>Tickets/accidents no problem</li><br>
    <li>Affordable insurance for college students</li>
  </ul>

  <div class="abs car-shadow" aria-hidden="true"></div>
  <div class="abs car-photo" role="img" aria-label="Photo of a white compact sedan, front three-quarter view"></div>

  <div class="abs brand">
    <div class="brand-mark"></div>
    <div class="brand-name">Meridian Crest<br>Insurance Services</div>
  </div>

  <p class="abs intro">We can provide full coverage, liability insurance and if you are having trouble affording car insurance please ask about our california state low cost insurance policy. If you have medical card and/or food stamp card then you are already pre qualified.</p>

  <h2 class="abs services-title">We Proide</h2>
  <ul class="abs services">
    <li>Auto Insurance</li>
    <li>Motorcycle insurance</li>
    <li>Renters insurance</li>
    <li>Homeowners insurance</li>
    <li class="more">and many more</li>
  </ul>

  <div class="abs card-photo card-benefits" role="img" aria-label="Photo of a state food benefits card"></div>
  <div class="abs card-photo card-id" role="img" aria-label="Photo of a state medical benefits identification card"></div>

  <div class="abs offices">
    <div class="offices-title">East Bay Area Offices In</div>
    <div class="offices-list">Oakland | Concord | Pittsburg | Antioch | Brentwood</div>
  </div>

  <div class="abs call">
    <div class="call-title">Call Us Now</div>
    <div class="call-phones">925-555-0142 | (510) 555-0187</div>
  </div>

  <div class="abs quote">
    <span class="quote-label">Get Quote On Our Website Now</span>
    <span class="quote-url">www.meridiancrestinsurance.com</span>
  </div>
</main>
</body>
</html>
```